Brovane Website re-design with new logo and look

Refresh on current website. Incorporate new logo which is attached. We provide technology SAAS services to the healthcare space. Current website is at brovane.com but the new name is Brovane.com (see logo) Key considerations are as follows:
1. Incorporate a promo video location. I have a new video coming out similar to this one. https://www.portfolink.net/gallery/41275063/Mobile-Application-Promo
2. Incorporate platform features section. as an example see this website where it has mini screens that call out various features ie; "all in one GCR platform" see webiste https://www.quendly.io/
3. Add some color splash from the log throughout the website
4. Where possible use the text from our website Brovane.com where not possible use lorem ipsum and we will complete
5. use current theme colors
6. Please use your skills to make it more functional and useful and not replicate what we have.

Target Market(s)

Imaging centers and hospitals

Industry/Entity Type

Healthcare

Coding

Coded - Design and coding required

Number of Pages Required

5+ page

Font styles to use
Sans Serif

Requirements
Must have
• Note section in this website that shows features of the platform as you scoll down. See website https://www.quendly.io/
Nice to have
• Professional look only, keep current color scheme but add in some splash of color from the logo
Should not have
• animated characters or cartoon drawings

```html
<!DOCTYPE html>
<html lang="en">
<head>
<meta charset="utf-8">
<title>Brovane — Technology for Healthcare</title>
<link href="https://fonts.googleapis.com/css2?family=Montserrat:wght@500;600;700;800&family=Roboto:wght@400;500;700&display=swap" rel="stylesheet">
<style>
:root{
  --ink:#1c1c1c;
  --body:#4a4a4a;
  --teal:#2a86ad;
  --teal-dark:#1e7ba0;
  --hero-a:#2447c4;
  --hero-b:#0c2585;
  --orange:#f28c2a;
  --orange-rule:#e2572a;
  --white:#ffffff;
  --footer:#121212;
  --soft-blue:#e9f0f8;
  --soft-peach:#fde9dd;
  --ui-blue:#2f6fe0;
  --ui-line:#e6eaf2;
  --ui-grey:#c9cfd9;
  --ui-red:#e8505b;
  --ui-green:#45b36b;
}
*{margin:0;padding:0;box-sizing:border-box}
html,body{width:1200px;height:4882px;overflow:hidden}
body{position:relative;font-family:'Roboto',sans-serif;color:var(--ink);background:var(--white)}
.abs{position:absolute}
h1,h2,h3,.brand,.nav a,.btn{font-family:'Montserrat',sans-serif}

/* header */
.site-header{position:absolute;top:0;left:0;width:1200px;height:83px;background:var(--white);border-bottom:1px solid #eee}
.brand{display:flex;align-items:center;gap:12px;font-weight:600;letter-spacing:3px;color:var(--ink);font-size:30px}
.brand .dot{width:30px;height:30px;border-radius:50%;background:var(--orange)}
.site-header .brand{position:absolute;left:112px;top:22px}
.nav{position:absolute;left:482px;top:0;height:83px;display:flex;align-items:center;gap:35px}
.nav a{font-size:14px;font-weight:600;color:var(--ink);text-decoration:none}
.nav a.active{color:var(--teal)}
.btn{display:inline-flex;align-items:center;justify-content:center;border-radius:22px;color:var(--white);font-weight:700;font-size:13px;text-decoration:none;background:linear-gradient(180deg,#3fa6c9,#1f7ba3)}
.nav .btn{width:140px;height:42px;margin-left:-2px}

/* hero */
.hero{position:absolute;top:83px;left:0;width:1200px;height:601px;background:linear-gradient(135deg,var(--hero-a),var(--hero-b))}
.hero h1{position:absolute;left:112px;top:160px;font-size:52px;line-height:64px;font-weight:800;color:var(--white);letter-spacing:1px}
.hero .tagline{position:absolute;left:112px;top:302px;color:var(--white);font-family:'Montserrat',sans-serif;font-weight:600;font-size:19px}
.hero .btn{position:absolute;left:112px;top:354px;width:142px;height:40px}
.play{position:absolute;left:262px;top:348px;width:52px;height:52px;border-radius:50%;background:rgba(255,255,255,.25);display:flex;align-items:center;justify-content:center}
.play span{width:34px;height:34px;border-radius:50%;background:var(--white);display:flex;align-items:center;justify-content:center}
.hero-art{position:absolute;left:480px;top:20px;width:720px;height:560px;background:radial-gradient(ellipse 300px 170px at 390px 285px,rgba(120,200,255,.7),rgba(60,120,235,.35) 55%,transparent 100%),radial-gradient(ellipse 360px 260px at 390px 285px,rgba(40,90,220,.5),transparent 100%)}

/* section headings */
.sec-head{position:absolute;left:0;width:1200px;text-align:center}
.sec-head .mark{width:34px;height:34px;border-radius:50%;background:var(--orange);margin:0 auto 16px}
.sec-head h2{font-size:30px;font-weight:700;letter-spacing:.5px}
.sec-head .rule{width:66px;height:3px;margin:12px auto 0;background:var(--teal)}

/* features */
.feature h3{font-size:26px;line-height:40px;font-weight:700;letter-spacing:.5px}
.feature p{margin-top:22px;font-size:14.5px;line-height:31px;color:var(--body)}
.screen{border-radius:14px;background:var(--white);box-shadow:0 10px 30px rgba(30,60,120,.15);overflow:hidden}
.screen svg{display:block}

/* solutions */
.solutions{position:absolute;top:1797px;left:0;width:1200px;height:538px;background:var(--teal-dark)}
.solutions .sec-head h2,.markets .sec-head h2{color:var(--white)}
.solutions .sec-head .rule,.markets .sec-head .rule{background:var(--white)}
.sol{position:absolute;top:208px;width:240px;text-align:center;color:var(--white)}
.sol .icon{width:96px;height:96px;border-radius:50%;background:var(--white);margin:0 auto;display:flex;align-items:center;justify-content:center}
.sol .icon i{display:block;width:52px;height:52px;border-radius:10px;background:linear-gradient(135deg,#cde6f2,#f9d2b2)}
.sol h3{margin-top:28px;font-size:21px;font-weight:700}
.sol p{margin-top:8px;font-size:14.5px;line-height:28px;color:#e2f1f8}
.sol a{display:inline-block;margin-top:6px;color:var(--white);font-weight:700;font-size:15px;text-decoration:underline}

/* purpose */
.purpose h2{position:absolute;left:112px;top:2432px;font-size:32px;line-height:41px;font-weight:700}
.purpose .rule{position:absolute;left:112px;top:2525px;width:100px;height:3px;background:var(--orange-rule)}
.purpose p{position:absolute;left:112px;top:2553px;width:440px;font-size:14.5px;line-height:31px;color:var(--body)}

/* markets */
.markets{position:absolute;top:2906px;left:0;width:1200px;height:577px;background:var(--orange)}
.mcard{position:absolute;top:201px;width:302px;height:283px;background:var(--white);border-radius:12px;overflow:hidden}
.mcard .ph{height:198px}
.mcard h3{position:absolute;left:22px;top:230px;font-size:18px;font-weight:700}
.mcard svg{position:absolute;right:20px;top:232px}
.arrow-btn{position:absolute;top:3233px;width:28px;height:28px;border-radius:50%;border:1.5px solid rgba(255,255,255,.8);display:flex;align-items:center;justify-content:center}

/* case studies */
.case{position:absolute;width:458px;height:274px;background:var(--white);box-shadow:0 6px 24px rgba(0,0,0,.08)}
.case .ph{position:absolute;left:0;top:0;width:243px;height:274px}
.case h3{position:absolute;left:274px;width:160px;font-family:'Roboto',sans-serif;font-size:15.5px;line-height:30px;font-weight:500}
.case .btn{position:absolute;left:274px;width:118px;height:36px;font-size:12px}

/* footer */
.site-footer{position:absolute;top:4415px;left:0;width:1200px;height:467px;background:var(--footer);color:var(--white)}
.site-footer .brand{position:absolute;left:0;width:1200px;justify-content:center;top:100px;color:var(--white);font-size:44px;gap:16px}
.site-footer .brand .dot{width:40px;height:40px}
.fnav{position:absolute;top:212px;left:0;width:1200px;display:flex;justify-content:center;gap:54px}
.fnav a{color:var(--white);font-family:'Roboto',sans-serif;font-size:15px;text-decoration:none}
.contact{position:absolute;top:280px;display:flex;align-items:center;gap:18px;font-size:15px}
.contact .ic{width:48px;height:48px;background:var(--teal);display:flex;align-items:center;justify-content:center}
.copy{position:absolute;top:384px;left:0;width:1200px;text-align:center;font-size:15px}
.copy span{color:var(--teal)}
</style>
</head>
<body>

<header class="site-header">
  <div class="brand"><span class="dot"></span>BROVANE</div>
  <nav class="nav">
    <a class="active" href="#">HOME</a>
    <a href="#">SOLUTIONS</a>
    <a href="#">MARKETS</a>
    <a href="#">CASE STUDIES</a>
    <a class="btn" href="#">CONTACT US</a>
  </nav>
</header>

<section class="hero">
  <div class="hero-art" role="img" aria-label="Glowing cloud network illustration with connected data cubes"></div>
  <h1>WELCOME TO<br>BROVANE</h1>
  <p class="tagline">TECHNOLOGY FOR HEALTHCARE</p>
  <a class="btn" href="#">GET STARTED</a>
  <div class="play"><span><svg width="14" height="14" viewBox="0 0 14 14"><path d="M3 1 L12 7 L3 13 Z" fill="#1f4fc0"/></svg></span></div>
</section>

<div class="sec-head" style="top:762px"><div class="mark"></div><h2>OUR FEATURES</h2></div>

<div class="abs" style="left:858px;top:866px;width:264px;height:306px;border-radius:16px;background:var(--soft-blue)"></div>
<div class="abs screen" style="left:620px;top:896px;width:468px;height:312px">
  <svg width="468" height="312" viewBox="0 0 468 312" aria-label="Dashboard with bar, line and donut charts">
    <rect x="0" y="0" width="96" height="312" fill="#f7f9fc"/>
    <circle cx="48" cy="36" r="12" fill="none" stroke="var(--ui-blue)" stroke-width="2"/>
    <circle cx="48" cy="33" r="4" fill="var(--ui-blue)"/>
    <rect x="22" y="66" width="48" height="5" rx="2" fill="var(--ui-grey)"/>
    <rect x="14" y="86" width="70" height="14" rx="4" fill="var(--ui-blue)"/>
    <rect x="22" y="112" width="44" height="5" rx="2" fill="var(--ui-grey)"/>
    <rect x="22" y="130" width="50" height="5" rx="2" fill="var(--ui-grey)"/>
    <rect x="22" y="148" width="40" height="5" rx="2" fill="var(--ui-grey)"/>
    <rect x="22" y="288" width="34" height="5" rx="2" fill="var(--ui-grey)"/>
    <rect x="108" y="10" width="60" height="6" rx="2" fill="#333"/>
    <g fill="var(--ui-blue)">
      <rect x="112" y="58" width="5" height="22"/><rect x="120" y="64" width="5" height="16"/><rect x="128" y="52" width="5" height="28"/><rect x="136" y="66" width="5" height="14"/><rect x="144" y="60" width="5" height="20"/><rect x="152" y="70" width="5" height="10"/><rect x="160" y="56" width="5" height="24"/><rect x="168" y="62" width="5" height="18"/><rect x="176" y="50" width="5" height="30"/><rect x="184" y="66" width="5" height="14"/><rect x="192" y="58" width="5" height="22"/><rect x="200" y="64" width="5" height="16"/><rect x="208" y="54" width="5" height="26"/><rect x="216" y="60" width="5" height="20"/><rect x="224" y="48" width="5" height="32"/><rect x="232" y="56" width="5" height="24"/><rect x="240" y="44" width="5" height="36"/><rect x="248" y="52" width="5" height="28"/><rect x="256" y="40" width="5" height="40"/><rect x="264" y="50" width="5" height="30"/><rect x="272" y="46" width="5" height="34"/>
    </g>
    <line x1="108" y1="81" x2="290" y2="81" stroke="var(--ui-line)"/>
    <g fill="none" stroke="var(--ui-line)"><rect x="304" y="26" width="58" height="64"/><line x1="304" y1="42" x2="362" y2="42"/><line x1="304" y1="58" x2="362" y2="58"/><line x1="304" y1="74" x2="362" y2="74"/></g>
    <rect x="340" y="74" width="10" height="16" fill="var(--ui-blue)"/>
    <rect x="370" y="38" width="86" height="14" rx="4" fill="var(--ui-blue)"/>
    <rect x="370" y="58" width="86" height="14" rx="4" fill="var(--ui-blue)" opacity=".8"/>
    <rect x="370" y="78" width="86" height="14" rx="4" fill="var(--ui-blue)" opacity=".6"/>
    <line x1="108" y1="172" x2="290" y2="172" stroke="var(--ui-line)"/>
    <polyline points="112,140 130,128 148,150 166,134 184,156 202,126 220,146 238,132 256,150 274,130 288,142" fill="none" stroke="var(--ui-red)" stroke-width="1.5"/>
    <polyline points="112,160 130,150 148,162 166,148 184,160 202,152 220,164 238,150 256,158 274,146 288,156" fill="none" stroke="var(--ui-blue)" stroke-width="1.5"/>
    <g fill="none" stroke-width="5">
      <circle cx="316" cy="126" r="11" stroke="var(--ui-line)"/><path d="M316 115a11 11 0 0 1 10 16" stroke="var(--ui-blue)"/>
      <circle cx="366" cy="126" r="11" stroke="var(--ui-line)"/><path d="M366 115a11 11 0 1 1-10 6" stroke="var(--ui-red)"/>
      <circle cx="316" cy="162" r="11" stroke="var(--ui-line)"/><path d="M316 151a11 11 0 1 1-11 11" stroke="var(--ui-green)"/>
      <circle cx="366" cy="162" r="11" stroke="var(--ui-line)"/><path d="M366 151a11 11 0 0 1 11 11" stroke="var(--ui-blue)"/>
    </g>
    <g fill="var(--ui-grey)"><rect x="400" y="118" width="50" height="4" rx="2"/><rect x="400" y="130" width="40" height="4" rx="2"/><rect x="400" y="154" width="50" height="4" rx="2"/><rect x="400" y="166" width="36" height="4" rx="2"/></g>
    <rect x="108" y="202" width="90" height="94" rx="4" fill="none" stroke="var(--ui-line)"/>
    <g fill="var(--ui-red)"><rect x="116" y="262" width="5" height="26"/><rect x="132" y="250" width="5" height="38"/><rect x="148" y="270" width="5" height="18"/><rect x="164" y="256" width="5" height="32"/><rect x="180" y="266" width="5" height="22"/></g>
    <g fill="var(--ui-blue)"><rect x="123" y="254" width="5" height="34"/><rect x="139" y="268" width="5" height="20"/><rect x="155" y="246" width="5" height="42"/><rect x="171" y="262" width="5" height="26"/><rect x="187" y="258" width="5" height="30"/></g>
    <rect x="206" y="202" width="84" height="94" rx="4" fill="none" stroke="var(--ui-line)"/>
    <g fill="var(--ui-grey)"><rect x="214" y="214" width="60" height="4" rx="2"/><rect x="214" y="228" width="50" height="4" rx="2"/><rect x="214" y="242" width="64" height="4" rx="2"/><rect x="214" y="256" width="44" height="4" rx="2"/></g>
    <circle cx="336" cy="252" r="26" fill="none" stroke="var(--ui-line)" stroke-width="6"/>
    <path d="M336 226a26 26 0 1 1-24 34" fill="none" stroke="var(--ui-blue)" stroke-width="6" stroke-dasharray="6 3"/>
    <path d="M312 260a26 26 0 0 1 8-28" fill="none" stroke="var(--ui-red)" stroke-width="6"/>
    <circle cx="420" cy="252" r="26" fill="none" stroke="var(--ui-green)" stroke-width="7"/>
    <path d="M420 226a26 26 0 0 1 26 26" fill="none" stroke="var(--orange)" stroke-width="7"/>
    <path d="M446 252a26 26 0 0 1-14 23" fill="none" stroke="var(--ui-red)" stroke-width="7"/>
  </svg>
</div>
<div class="feature abs" style="left:112px;top:952px;width:440px">
  <h3>STREAMLINED PATIENT DATA MANAGEMENT</h3>
  <p>Lorem ipsum dolor sit amet, consectetur adipiscing elit, sed do eiusmod tempor incididunt ut labore et dolore magna aliqua. Ut enim ad minim veniam, quis nostrud exercitation ullamco laboris nisi ut aliquip ex ea commodo consequat.</p>
</div>

<div class="abs" style="left:344px;top:1328px;width:268px;height:254px;border-radius:16px;background:var(--soft-peach)"></div>
<div class="abs screen" style="left:110px;top:1354px;width:470px;height:314px">
  <svg width="470" height="314" viewBox="0 0 470 314" aria-label="Analytics screen with line charts and tables">
    <rect x="0" y="0" width="470" height="20" fill="#f4f5f7"/>
    <rect x="0" y="20" width="74" height="294" fill="#f7f9fc"/>
    <rect x="10" y="30" width="40" height="5" rx="2" fill="#333"/>
    <rect x="8" y="62" width="58" height="10" rx="3" fill="var(--ui-green)"/>
    <g fill="var(--ui-grey)"><rect x="14" y="46" width="40" height="4" rx="2"/><rect x="14" y="82" width="36" height="4" rx="2"/><rect x="14" y="98" width="42" height="4" rx="2"/><rect x="14" y="114" width="34" height="4" rx="2"/><rect x="14" y="130" width="40" height="4" rx="2"/><rect x="14" y="146" width="38" height="4" rx="2"/><rect x="14" y="162" width="32" height="4" rx="2"/></g>
    <rect x="84" y="30" width="50" height="5" rx="2" fill="#333"/>
    <g fill="none" stroke="var(--ui-line)"><rect x="84" y="44" width="118" height="56" rx="4"/><rect x="212" y="44" width="118" height="56" rx="4"/><rect x="340" y="44" width="118" height="56" rx="4"/></g>
    <g fill="none" stroke="var(--ui-green)" stroke-width="1.5">
      <polyline points="90,92 110,88 124,80 136,60 148,80 162,88 196,92"/>
      <polyline points="218,92 238,88 252,78 264,58 276,78 290,88 324,92"/>
      <polyline points="346,92 366,88 380,80 392,62 404,80 418,88 452,92"/>
    </g>
    <rect x="84" y="110" width="246" height="110" rx="4" fill="none" stroke="var(--ui-line)"/>
    <g stroke="var(--ui-line)"><line x1="96" y1="140" x2="230" y2="140"/><line x1="96" y1="165" x2="230" y2="165"/><line x1="96" y1="190" x2="230" y2="190"/></g>
    <polyline points="96,170 110,150 124,180 138,140 152,175 166,150 180,185 194,145 208,170 222,155" fill="none" stroke="#888" stroke-width="1"/>
    <polyline points="96,180 110,165 124,158 138,178 152,150 166,172 180,160 194,178 208,150 222,168" fill="none" stroke="var(--ui-green)" stroke-width="1"/>
    <g><rect x="240" y="140" width="14" height="5" fill="var(--ui-green)"/><rect x="240" y="156" width="14" height="5" fill="var(--ui-green)" opacity=".6"/><rect x="240" y="172" width="14" height="5" fill="#333"/><rect x="240" y="188" width="14" height="5" fill="#888"/></g>
    <g fill="var(--ui-grey)"><rect x="260" y="140" width="50" height="4" rx="2"/><rect x="260" y="156" width="50" height="4" rx="2"/><rect x="260" y="172" width="50" height="4" rx="2"/><rect x="260" y="188" width="50" height="4" rx="2"/></g>
    <rect x="340" y="110" width="118" height="110" rx="4" fill="none" stroke="var(--ui-line)"/>
    <g fill="#444"><rect x="350" y="130" width="20" height="5"/><rect x="382" y="130" width="20" height="5"/><rect x="414" y="130" width="20" height="5"/></g>
    <polyline points="350,200 362,182 374,196 386,176 398,192 410,172 422,190 434,178 446,194" fill="none" stroke="var(--ui-green)" stroke-width="1.5"/>
    <rect x="84" y="230" width="186" height="74" rx="4" fill="none" stroke="var(--ui-line)"/>
    <rect x="92" y="240" width="30" height="5" rx="2" fill="#333"/>
    <g fill="var(--ui-grey)"><rect x="92" y="256" width="110" height="4" rx="2"/><rect x="92" y="272" width="110" height="4" rx="2"/></g>
    <rect x="92" y="264" width="150" height="3" fill="var(--ui-green)"/><rect x="92" y="280" width="120" height="3" fill="var(--ui-green)"/>
    <rect x="278" y="230" width="180" height="74" rx="4" fill="none" stroke="var(--ui-line)"/>
    <rect x="286" y="240" width="30" height="5" rx="2" fill="#333"/>
    <g fill="var(--ui-grey)"><rect x="286" y="256" width="16" height="4"/><rect x="310" y="256" width="30" height="4"/><rect x="350" y="256" width="30" height="4"/><rect x="286" y="272" width="16" height="4"/><rect x="310" y="272" width="30" height="4"/><rect x="350" y="272" width="30" height="4"/><rect x="286" y="288" width="16" height="4"/><rect x="310" y="288" width="30" height="4"/><rect x="350" y="288" width="30" height="4"/></g>
    <g fill="var(--ui-green)" opacity=".8"><rect x="392" y="254" width="24" height="8" rx="3"/><rect x="392" y="270" width="24" height="8" rx="3"/><rect x="392" y="286" width="24" height="8" rx="3"/></g>
    <g fill="var(--ui-grey)"><rect x="426" y="256" width="20" height="4"/><rect x="426" y="272" width="20" height="4"/><rect x="426" y="288" width="20" height="4"/></g>
  </svg>
</div>
<div class="feature abs" style="left:647px;top:1396px;width:450px">
  <h3>SEAMLESS INTEGRATION WITH HEALTHCARE SYSTEMS</h3>
  <p>Lorem ipsum dolor sit amet, consectetur adipiscing elit, sed do eiusmod tempor incididunt ut labore et dolore magna aliqua. Ut enim ad minim veniam, quis nostrud exercitation ullamco laboris nisi ut aliquip ex ea commodo consequat.</p>
</div>

<section class="solutions">
  <div class="sec-head" style="top:76px"><div class="mark"></div><h2>OUR SOLUTIONS</h2><div class="rule"></div></div>
  <div class="sol" style="left:94px"><div class="icon" role="img" aria-label="Teleradiology icon"><i></i></div><h3>Teleradiology</h3><p>End to End workflow to and<br>from anywhere</p><a href="#">View More</a></div>
  <div class="sol" style="left:353px"><div class="icon" role="img" aria-label="Clinical icon"><i></i></div><h3>Clinical</h3><p>Highly Subspecialized<br>Clinicians</p><a href="#">View More</a></div>
  <div class="sol" style="left:612px"><div class="icon" role="img" aria-label="Compliance icon"><i></i></div><h3>Compliance</h3><p>Integrated compliance across<br>various verticals</p><a href="#">View More</a></div>
  <div class="sol" style="left:871px"><div class="icon" role="img" aria-label="PACS/RIS icon"><i></i></div><h3>PACS/RIS</h3><p>Affordable PACS/RIS<br>replacement</p><a href="#">View More</a></div>
</section>

<section class="purpose">
  <h2>PURPOSE BUILT<br>TECHNOLOGY</h2>
  <div class="rule"></div>
  <p>Our end to end workflow platform is purposely built for remote access from anywhere in the world while providing centralized management access.Our end to end workflow platform is purposely built for remote access from anywhere in the world while providing &nbsp;centralized management access.</p>
  <div class="abs" style="left:906px;top:2429px;width:172px;height:140px;background:var(--orange-rule)"></div>
  <div class="abs" style="left:615px;top:2557px;width:314px;height:252px;border:2px solid var(--teal)"></div>
  <div class="abs" style="left:627px;top:2437px;width:444px;height:357px;background:linear-gradient(180deg,#c9d4dc,#6e7c86)" role="img" aria-label="Group photo of a diverse healthcare business team"></div>
</section>

<section class="markets">
  <div class="sec-head" style="top:76px"><div class="mark" style="background:var(--white)"></div><h2>MARKETS</h2><div class="rule"></div></div>
  <div class="mcard" style="left:112px"><div class="ph" role="img" aria-label="Hospital ward with beds" style="background:linear-gradient(180deg,#b8c6cf,#6f8593)"></div><h3>Hospitals</h3><svg width="30" height="14" viewBox="0 0 30 14"><path d="M0 7H28M22 1l6 6-6 6" fill="none" stroke="#222" stroke-width="1.6"/></svg></div>
  <div class="mcard" style="left:449px"><div class="ph" role="img" aria-label="Hand touching a digital medical interface" style="background:linear-gradient(135deg,#0f5a6e,#4fb3c2)"></div><h3>Urgent Care</h3><svg width="30" height="14" viewBox="0 0 30 14"><path d="M0 7H28M22 1l6 6-6 6" fill="none" stroke="#222" stroke-width="1.6"/></svg></div>
  <div class="mcard" style="left:786px"><div class="ph" role="img" aria-label="Government office towers at dusk" style="background:linear-gradient(180deg,#3a3f8e,#1c1f3a)"></div><h3>Government Health</h3><svg width="30" height="14" viewBox="0 0 30 14"><path d="M0 7H28M22 1l6 6-6 6" fill="none" stroke="#222" stroke-width="1.6"/></svg></div>
</section>
<div class="arrow-btn" style="left:44px"><svg width="10" height="10" viewBox="0 0 10 10"><path d="M7 1 3 5l4 4" fill="none" stroke="#fff" stroke-width="1.5"/></svg></div>
<div class="arrow-btn" style="left:1127px"><svg width="10" height="10" viewBox="0 0 10 10"><path d="M3 1l4 4-4 4" fill="none" stroke="#fff" stroke-width="1.5"/></svg></div>

<div class="sec-head" style="top:3578px"><div class="mark"></div><h2>CASE STUDIES</h2><div class="rule"></div></div>

<article class="case" style="left:112px;top:3724px">
  <div class="ph" role="img" aria-label="Government buildings at night" style="background:linear-gradient(180deg,#3b4190,#1b1e3a)"></div>
  <h3 style="top:68px">Government Deployment across 150 Locations</h3>
  <a class="btn" href="#" style="top:174px">READ MORE</a>
</article>
<article class="case" style="left:630px;top:3724px">
  <div class="ph" role="img" aria-label="Hands holding a tablet with clinical reports" style="background:linear-gradient(135deg,#9fb3c4,#3c5a78)"></div>
  <h3 style="top:92px">Predictive clinical Reporting</h3>
  <a class="btn" href="#" style="top:166px">READ MORE</a>
</article>
<article class="case" style="left:112px;top:4040px">
  <div class="ph" role="img" aria-label="Portrait of a smiling doctor" style="background:linear-gradient(135deg,#c9c7c2,#7d8a93)"></div>
  <h3 style="top:92px">Centralized Workflow Management</h3>
  <a class="btn" href="#" style="top:166px">READ MORE</a>
</article>
<article class="case" style="left:630px;top:4040px">
  <div class="ph" role="img" aria-label="Skyscrapers viewed from below" style="background:linear-gradient(160deg,#cfd6de,#2c3440)"></div>
  <h3 style="top:92px">Integration across disparate systems</h3>
  <a class="btn" href="#" style="top:166px">READ MORE</a>
</article>

<footer class="site-footer">
  <div class="brand"><span class="dot"></span>BROVANE</div>
  <nav class="fnav"><a href="#">HOME</a><a href="#">SOLUTIONS</a><a href="#">MARKETS</a><a href="#">CASE STUDIES</a><a href="#">CONTACT US</a></nav>
  <div class="contact" style="left:190px"><span class="ic"><svg width="22" height="16" viewBox="0 0 22 16"><rect width="22" height="16" rx="2" fill="#fff"/><path d="M1 2l10 7 10-7" fill="none" stroke="#2a86ad" stroke-width="1.8"/></svg></span>info@brovane.com</div>
  <div class="contact" style="left:482px"><span class="ic"><svg width="16" height="22" viewBox="0 0 16 22"><path d="M8 0a8 8 0 0 1 8 8c0 6-8 14-8 14S0 14 0 8a8 8 0 0 1 8-8z" fill="#fff"/><circle cx="8" cy="8" r="3" fill="#2a86ad"/></svg></span>BROVANE,UNITED STATE.</div>
  <div class="contact" style="left:838px"><span class="ic"><svg width="20" height="20" viewBox="0 0 20 20"><path d="M4 1l4 4-2 3c1 3 3 5 6 6l3-2 4 4-3 3C8 19 1 12 1 4z" fill="#fff"/></svg></span>1-555-014-2290</div>
  <p class="copy">Copyrights@2024.<span>BROVANE</span>.All Rights Reserved</p>
</footer>

</body>
</html>
```